Business Card Design

A new interior design company specialising in residential property styling, with a focus on styling properties for sale. We aim to present the property to increase marketability, saleability and hopefully get the best price.
We are looking for a design that stands out from the crowd maybe using colour and maybe pattern, something that is modern and fits in with companies aesthetic of design.
We would like the design not to be too fussy, with perhaps all of the contact information on the back (ie just the company name on front?)

Industry/Entity Type

Residential

Contact Information for Business Card

Brisa Interiors, Tessa Wingrove, Interior Designer,0417365209, brisainteriors@quolmail.com.au

Requirements
Nice to have
• Brisa means "love" in Spanish and I was wondering whether it might be too corny to use the M in bRisa that resembles a love heart, something curvy. This is just an idea I've was toying with and I am completely open to other suggestions.

```html
<!DOCTYPE html>
<html lang="en">
<head>
<meta charset="utf-8">
<title>Brisa Interiors – Business Card</title>
<link href="https://fonts.googleapis.com/css2?family=Open+Sans:wght@400;600&display=swap" rel="stylesheet">
<style>
  :root {
    --page-bg: #ffffff;
    --cream: #f6ecc8;
    --cream-light: #fbf4dc;
    --rust: #b2471c;
    --rust-deep: #a23a12;
    --orange: #d96a2a;
    --orange-soft: #e89250;
    --white: #ffffff;
  }
  html, body {
    margin: 0;
    width: 1200px;
    height: 900px;
    overflow: hidden;
    background: var(--page-bg);
    font-family: "Open Sans", Arial, sans-serif;
  }
  .card {
    position: absolute;
    left: 100px;
    top: 145px;
    width: 1000px;
    height: 610px;
    border-radius: 34px;
    overflow: hidden;
    background:
      linear-gradient(to bottom,
        var(--cream-light) 0%,
        var(--cream) 48%,
        var(--orange-soft) 68%,
        var(--orange) 84%,
        var(--rust-deep) 100%);
    box-shadow: 0 2px 6px rgba(0,0,0,0.08);
  }
  .stripe {
    position: absolute;
    top: 20px;
    bottom: 0;
    background: linear-gradient(to bottom,
      rgba(214, 110, 50, 0) 0%,
      rgba(214, 110, 50, 0.35) 35%,
      rgba(190, 80, 30, 0.55) 70%,
      rgba(160, 60, 20, 0.3) 100%);
  }
  .stripe--a { left: 40px;  width: 10px; }
  .stripe--b { left: 70px;  width: 40px; top: 60px; }
  .stripe--c { left: 290px; width: 18px; }
  .stripe--d { left: 350px; width: 45px; top: 120px; }
  .stripe--e { left: 540px; width: 30px; top: 90px; }
  .stripe--f { left: 600px; width: 12px; }
  .stripe--g { left: 735px; width: 55px; top: 140px; }
  .stripe--h { left: 830px; width: 16px; }
  .stripe--i { left: 905px; width: 40px; top: 170px; }

  .ornament {
    position: absolute;
  }
  .ornament--upper-left {
    left: 40px;
    top: 110px;
    width: 300px;
    height: 240px;
    background: radial-gradient(ellipse at center,
      rgba(196, 104, 54, 0.35) 0%,
      rgba(196, 104, 54, 0) 70%);
  }
  .ornament--lower-right {
    left: 600px;
    top: 300px;
    width: 400px;
    height: 310px;
    background: radial-gradient(ellipse at center,
      rgba(150, 55, 15, 0.35) 0%,
      rgba(150, 55, 15, 0) 70%);
  }

  .contact-person {
    position: absolute;
    right: 70px;
    top: 52px;
    text-align: right;
    color: var(--rust);
  }
  .contact-person__name {
    margin: 0;
    font-size: 25px;
    font-weight: 400;
    line-height: 1.2;
  }
  .contact-person__role {
    margin: 2px 0 0;
    font-size: 16px;
    font-weight: 400;
  }

  .brand-name {
    position: absolute;
    left: 0;
    right: 0;
    top: 200px;
    margin: 0;
    text-align: center;
    font-size: 84px;
    font-weight: 400;
    color: var(--rust);
    letter-spacing: 1px;
  }

  .contact-list {
    position: absolute;
    left: 68px;
    bottom: 52px;
    margin: 0;
    padding: 0;
    list-style: none;
    color: var(--white);
    font-size: 29px;
    line-height: 1.35;
  }
  .contact-list__item {
    display: flex;
    align-items: center;
    gap: 12px;
  }
  .contact-list__icon {
    width: 24px;
    height: 24px;
    flex: none;
  }
</style>
</head>
<body>
  <section class="card" aria-label="Brisa Interiors business card">
    <div class="stripe stripe--a"></div>
    <div class="stripe stripe--b"></div>
    <div class="stripe stripe--c"></div>
    <div class="stripe stripe--d"></div>
    <div class="stripe stripe--e"></div>
    <div class="stripe stripe--f"></div>
    <div class="stripe stripe--g"></div>
    <div class="stripe stripe--h"></div>
    <div class="stripe stripe--i"></div>

    <div class="ornament ornament--upper-left" role="img" aria-label="Curling floral swirl ornament in soft rust tones"></div>
    <div class="ornament ornament--lower-right" role="img" aria-label="Curling floral swirl ornament in deep rust tones"></div>

    <div class="contact-person">
      <p class="contact-person__name">Tessa Wingrove</p>
      <p class="contact-person__role">Interior Designer</p>
    </div>

    <h1 class="brand-name">Brisa Interiors</h1>

    <ul class="contact-list">
      <li class="contact-list__item">
        <svg class="contact-list__icon" viewBox="0 0 24 24" aria-hidden="true">
          <path fill="#ffffff" d="M6.6 10.8c1.4 2.8 3.8 5.1 6.6 6.6l2.2-2.2c.3-.3.7-.4 1-.2 1.1.4 2.3.6 3.6.6.6 0 1 .4 1 1V20c0 .6-.4 1-1 1C10.6 21 3 13.4 3 4c0-.6.4-1 1-1h3.5c.6 0 1 .4 1 1 0 1.3.2 2.5.6 3.6.1.3 0 .7-.2 1L6.6 10.8z"/>
        </svg>
        <span>0417365209</span>
      </li>
      <li class="contact-list__item">
        <svg class="contact-list__icon" viewBox="0 0 24 24" aria-hidden="true">
          <rect x="2" y="5" width="20" height="14" rx="2" fill="#ffffff"/>
          <path d="M3 6.5l9 6.5 9-6.5" fill="none" stroke="#c4561f" stroke-width="1.8"/>
        </svg>
        <span>brisainteriors@quolmail.com.au</span>
      </li>
    </ul>
  </section>
</body>
</html>
```